Craft Instant Coffee Box Packaging design

We need packaging designed for our craft instant coffee. Needs to be simple yet eye-catching. We are looking to package instant coffee sachets inside a cigarette style box. Front of box must make it clear that it is instant coffee and show contents - 7 pack / 21g net as well as Brindle Oak Coffee Co. which is the company name. We'd prefer the instant coffee be the focal point rather than the company name. The rear will have 'ingredients', company address and barcode. Sides should either state contents such as 'Instant Coffee' or company name.

Font styles to use
Sans Serif

Colors

Designer to choose colors to be used in the design.

Requirements
Must have
• Front of box must make it clear that it is instant coffee and show contents - 7 pack / 21g net as well as Brindle Oak Coffee Co. which is the company name. We'd prefer the instant coffee be the focal point rather than the company name. The rear will have 'ingredients', company address and barcode. Sides should either state contents such as 'Instant Coffee' or company name.
Nice to have
• modern colour scheme - 'Brindle Oak Coffee Co.' in a simple sans serif font
Should not have
• Must not be too 'busy' or 'cheap' looking

```html
<!DOCTYPE html>
<html lang="en">
<head>
<meta charset="utf-8">
<title>Brindle Oak Coffee Co. – Instant Coffee Box Dieline</title>
<link rel="stylesheet" href="https://fonts.googleapis.com/css2?family=Montserrat:wght@300;800;900&family=Open+Sans:wght@400;600&display=swap">
<style>
  :root {
    --orange-light: #f07026;
    --orange-mid: #e2602a;
    --orange-deep: #cf522c;
    --charcoal: #242223;
    --ink: #231a17;
    --coral: #ec5b4c;
    --rust: #c44a2a;
  }
  * { margin: 0; padding: 0; box-sizing: border-box; }
  html, body { width: 1200px; height: 933px; overflow: hidden; }
  body { background: var(--orange-mid); }
  .dieline { position: relative; width: 1200px; height: 933px; overflow: hidden; }
  .dieline-shapes { position: absolute; inset: 0; }

  .brand, .product-title, .side-label, .ingredients, .net-contents {
    position: absolute;
  }
  .brand { left: 566px; width: 400px; text-align: center; }
  .brand-name {
    font-family: "Montserrat", sans-serif; font-weight: 900;
    letter-spacing: 4px; color: var(--ink); line-height: 1;
  }
  .brand-sub {
    font-family: "Montserrat", sans-serif; font-weight: 300;
    letter-spacing: 4px; color: var(--ink); line-height: 1;
  }
  .brand--lid { top: 48px; }
  .brand--lid .brand-name { font-size: 34px; }
  .brand--lid .brand-sub { font-size: 18px; margin-top: 6px; }
  .brand--base { top: 836px; }
  .brand--base .brand-name { font-size: 34px; }
  .brand--base .brand-sub { font-size: 18px; margin-top: 6px; }
  .brand--front { top: 524px; }
  .brand--front .brand-name { font-size: 23px; color: var(--coral); letter-spacing: 3px; }
  .brand--front .brand-sub { font-size: 15px; color: var(--rust); margin-top: 9px; }

  .product-title {
    left: 566px; width: 400px; top: 209px; text-align: center;
    font-family: "Montserrat", sans-serif; font-weight: 900;
    font-size: 29px; letter-spacing: 3px; color: var(--ink);
  }
  .side-label {
    top: 482px; width: 300px; margin-left: -150px; text-align: center;
    transform: rotate(-90deg); transform-origin: center;
    font-family: "Open Sans", sans-serif; font-weight: 600;
    font-size: 30px; letter-spacing: 3px; color: var(--orange-light);
    line-height: 1; margin-top: -15px;
  }
  .side-label--left { left: 476px; }
  .side-label--right { left: 1041px; }

  .ingredients { left: 65px; top: 260px; color: var(--orange-light); font-family: "Open Sans", sans-serif; }
  .ingredients-title { font-size: 18px; font-weight: 600; letter-spacing: 3px; }
  .ingredients-body { margin-top: 14px; font-size: 16px; letter-spacing: 2px; line-height: 26.5px; }

  .net-contents {
    left: 566px; width: 400px; top: 742px; text-align: center;
    font-family: "Open Sans", sans-serif; font-size: 18px;
    letter-spacing: -0.5px; color: var(--ink);
  }
</style>
</head>
<body>
<main class="dieline">
  <svg class="dieline-shapes" width="1200" height="933" viewBox="0 0 1200 933">
    <defs>
      <linearGradient id="board" x1="0" y1="0" x2="1" y2="0">
        <stop offset="0" stop-color="#f27127"/>
        <stop offset="1" stop-color="#d9582a"/>
      </linearGradient>
      <linearGradient id="lidBand" x1="0" y1="0" x2="1" y2="0">
        <stop offset="0" stop-color="#ef6d25"/>
        <stop offset="1" stop-color="#cc4f2c"/>
      </linearGradient>
      <radialGradient id="frontArt" cx="0.5" cy="0.45" r="0.6">
        <stop offset="0" stop-color="#f07a2a"/>
        <stop offset="1" stop-color="#cf4e26"/>
      </radialGradient>
    </defs>
    <rect class="board" width="1200" height="933" fill="url(#board)"/>
    <polygon class="lid-flap" points="0,0 1200,0 1200,176 1112,152 0,152" fill="url(#lidBand)" opacity="0.55"/>
    <polygon class="box-panels" points="0,228 404,228 552,302 964,302 1112,228 1200,228 1200,722 0,722" fill="var(--charcoal)"/>
    <rect class="front-art" x="678" y="302" width="180" height="200" fill="url(#frontArt)"
          role="img" aria-label="Illustration of a coffee bean dissolving into grounds"/>
  </svg>

  <div class="brand brand--lid">
    <div class="brand-name">BRINDLE OAK</div>
    <div class="brand-sub">Coffee Co</div>
  </div>

  <div class="product-title">INSTANT COFFEE</div>

  <section class="ingredients">
    <h2 class="ingredients-title">Ingredients</h2>
    <p class="ingredients-body">Lorem ipsum dolor sit amet,<br>consectetuer adipiscing elit,<br>sed diam nonummy nibh<br>euismod tincidunt ut laoreet<br>dolore magna aliquam erat<br>volutpat. Ut wisi enim ad</p>
  </section>

  <div class="side-label side-label--left">INSTANT COFFEE</div>
  <div class="side-label side-label--right">INSTANT COFFEE</div>

  <div class="brand brand--front">
    <div class="brand-name">BRINDLE OAK</div>
    <div class="brand-sub">Coffee Co</div>
  </div>

  <div class="net-contents">7 pack / 21g net</div>

  <div class="brand brand--base">
    <div class="brand-name">BRINDLE OAK</div>
    <div class="brand-sub">Coffee Co</div>
  </div>
</main>
</body>
</html>
```